Business Card Design Project

Need a business card which is crisp, clear and modern.
with the logo being highlighted and at the back of the card our services.
Please use the attached logo for creating the cards.

Reason: need to receive some good designs

Target Market(s)

Our target customers will be hotels, offices, single users

Industry/Entity Type

Business

```html
<!DOCTYPE html>
<html lang="en">
<head>
<meta charset="utf-8">
<title>Linkora Business Card</title>
<link rel="stylesheet" href="https://fonts.googleapis.com/css2?family=Open+Sans:wght@400;600;700&family=Arimo:wght@700&display=swap">
<style>
  :root {
    --stage: #d9d9d9;
    --card: #f4f4f4;
    --card-edge: #e6e6e6;
    --ink: #111111;
    --text-grey: #6a6a6a;
    --band: #2f2f2f;
    --accent-lime: #d4e000;
    --icon-green: #8cc63f;
    --icon-red: #e2231a;
    --icon-blue: #1ea0d8;
    --white: #ffffff;
  }
  * { box-sizing: border-box; margin: 0; padding: 0; }
  html, body { width: 1200px; height: 900px; overflow: hidden; }
  body {
    background: var(--stage);
    font-family: "Open Sans", Arial, sans-serif;
    display: flex;
    flex-direction: column;
    align-items: center;
    justify-content: center;
    gap: 40px;
  }
  .card {
    position: relative;
    width: 700px;
    height: 390px;
    background: linear-gradient(135deg, var(--white) 0%, var(--card) 55%, var(--card-edge) 100%);
    box-shadow: 0 6px 18px rgba(0,0,0,0.18);
    overflow: hidden;
  }
  /* Back */
  .card-back {
    display: flex;
    flex-direction: column;
    align-items: center;
    justify-content: center;
    gap: 18px;
  }
  .brand-back {
    display: flex;
    align-items: center;
    gap: 14px;
    font-weight: 700;
    font-size: 54px;
    color: var(--ink);
    letter-spacing: 1px;
  }
  .brand-dot {
    width: 40px;
    height: 40px;
    border-radius: 50%;
    background: var(--icon-blue);
  }
  .back-web {
    font-size: 22px;
    letter-spacing: 3px;
    color: var(--text-grey);
  }
  /* Front */
  .brand-front {
    position: absolute;
    left: 44px;
    top: 46px;
    display: flex;
    align-items: center;
    gap: 12px;
    font-weight: 700;
    font-size: 46px;
    color: var(--ink);
  }
  .brand-front .brand-dot { width: 34px; height: 34px; }
  .address {
    position: absolute;
    left: 46px;
    top: 170px;
    font-size: 17px;
    line-height: 1.4;
    color: var(--text-grey);
    font-weight: 600;
  }
  .contacts {
    position: absolute;
    left: 46px;
    top: 250px;
    list-style: none;
    display: flex;
    flex-direction: column;
    gap: 8px;
    font-size: 19px;
    color: var(--text-grey);
  }
  .contacts li { display: flex; align-items: center; gap: 10px; }
  .contacts svg { width: 22px; height: 22px; flex: none; }
  .name-band {
    position: absolute;
    right: 0;
    top: 118px;
    width: 250px;
    height: 34px;
    background: var(--band);
    display: flex;
    align-items: center;
    padding-left: 16px;
  }
  .person-name {
    font-family: "Arimo", Arial, sans-serif;
    font-size: 22px;
    color: var(--accent-lime);
  }
  .person-role {
    position: absolute;
    right: 140px;
    top: 156px;
    font-size: 14px;
    font-weight: 700;
    color: var(--ink);
    letter-spacing: 0.5px;
  }
  .web-band {
    position: absolute;
    right: 0;
    top: 228px;
    width: 250px;
    height: 34px;
    background: var(--band);
    display: flex;
    align-items: center;
    padding-left: 16px;
    font-size: 17px;
    color: var(--white);
  }
</style>
</head>
<body>
  <section class="card card-back">
    <div class="brand-back"><span class="brand-dot"></span>Linkora</div>
    <div class="back-web">www.linkora.com</div>
  </section>

  <section class="card card-front">
    <div class="brand-front"><span class="brand-dot"></span>Linkora</div>

    <p class="address">street#48120 north side Harbour Lane,<br>Toronto, Canada</p>

    <ul class="contacts">
      <li>
        <svg viewBox="0 0 22 22" aria-hidden="true"><circle cx="11" cy="11" r="11" fill="var(--icon-green)"/><path d="M6 9c0-2 2-3 5-3s5 1 5 3l-2 1-1-2h-4l-1 2zM7 11h8l1 5H6z" fill="#fff"/></svg>
        xxx-xxx-xxxx
      </li>
      <li>
        <svg viewBox="0 0 22 22" aria-hidden="true"><circle cx="11" cy="11" r="11" fill="var(--icon-red)"/><rect x="8" y="5" width="6" height="12" rx="1" fill="none" stroke="#fff" stroke-width="1.5"/><circle cx="11" cy="15" r="0.8" fill="#fff"/></svg>
        xxx-xxx-xxxx
      </li>
      <li>
        <svg viewBox="0 0 22 22" aria-hidden="true"><circle cx="11" cy="11" r="11" fill="var(--icon-blue)"/><text x="11" y="15" text-anchor="middle" font-size="12" font-family="Arial, sans-serif" fill="#fff">@</text></svg>
        info@linkora.com
      </li>
    </ul>

    <div class="name-band"><span class="person-name">Daniel Marsh</span></div>
    <div class="person-role">President</div>

    <div class="web-band">www.linkora.com</div>
  </section>
</body>
</html>
```